New Flyer Design Project

Needing brochure explaining the benefits of a home sleep study compared to a clinical hospital sleep study. We had our company logo designed by Lumen Forge, we love it. We would like for it to be a bi-fold. See attachments for examples of information we would like to include.

```html
<!DOCTYPE html>
<html lang="en">
<head>
<meta charset="utf-8">
<title>Harborline CPAP – Home Sleep Study Bi-fold</title>
<link href="https://fonts.googleapis.com/css2?family=Montserrat:wght@400;500;600;700;800&display=swap" rel="stylesheet">
<style>
:root{
  --navy:#163f78;
  --navy-deep:#0f2f5e;
  --blue:#1e63b0;
  --blue-box:#1b6bbd;
  --green:#3fae3c;
  --green-light:#6cc24a;
  --ink:#1b3a6b;
  --paper:#ffffff;
  --pale:#e8eff7;
  --stage:#d6d8db;
  --photo-warm:#e9e3de;
  --photo-cool:#c9d2dc;
}
*{box-sizing:border-box;margin:0;padding:0}
html,body{width:814px;height:1200px;overflow:hidden;background:var(--stage);font-family:'Montserrat',sans-serif}
.spread{position:absolute;left:20px;width:774px;height:548px;background:var(--paper);box-shadow:0 2px 10px rgba(0,0,0,.18);overflow:hidden}
.spread.outside{top:36px}
.spread.inside{top:616px}
.panel{position:absolute;top:0;width:387px;height:548px;overflow:hidden}
.panel.left{left:0}
.panel.right{left:387px}
.abs{position:absolute}
svg.abs{left:0;top:0}
.brand{position:absolute;font-weight:700;line-height:1.05;letter-spacing:.2px}
.brand small{display:block;font-size:.55em;letter-spacing:1.6px;font-weight:700}
.photo-frame{position:absolute;border:3px solid #fff;border-radius:6px}

/* back panel */
.back{background:linear-gradient(160deg,var(--navy) 0%,var(--navy-deep) 100%)}
.back .brand{left:40px;top:78px;color:#fff;font-size:15px}
.back .headline{left:40px;top:232px;width:310px;color:#fff;font-weight:800;font-size:15px;line-height:1.2}
.back .lede{left:40px;top:274px;width:270px;color:#dfe8f4;font-size:10.5px;line-height:1.35}
.back .rule{left:40px;top:332px;width:118px;height:2px;background:var(--green)}
.contact{position:absolute;left:40px;display:flex;align-items:center;gap:8px;color:#fff}
.contact svg{flex:none}
.contact.phone{top:348px;font-size:26px;font-weight:700}
.contact.web{top:390px;font-size:11px}
.contact.mail{top:414px;font-size:11px}
.contact.addr{top:438px;font-size:11px;align-items:flex-start;line-height:1.3}

/* front panel */
.front .brand{left:22px;top:30px;color:var(--blue);font-size:15px}
.front .title{left:0;width:387px;top:270px;text-align:center;font-weight:800;font-size:30px;line-height:1.02}
.front .title span{display:block}
.front .title .l1{color:var(--navy)}
.front .title .l2{color:var(--green)}
.front .tagline{left:0;width:387px;top:342px;text-align:center;color:var(--ink);font-size:9.5px;font-weight:600}
.front .facts{left:40px;top:366px;width:300px;height:72px;border-radius:8px;background:linear-gradient(90deg,#e3ecf6,#f4f7fb);padding:10px 14px}
.tick-list{list-style:none}
.tick-list li{display:flex;align-items:center;gap:7px;font-size:9.5px;font-weight:700;color:var(--ink);margin-bottom:5px}
.tick{width:10px;height:10px;border-radius:50%;background:var(--green);flex:none;position:relative}
.tick::after{content:"";position:absolute;left:3px;top:1.5px;width:3px;height:5px;border:solid #fff;border-width:0 1.5px 1.5px 0;transform:rotate(45deg)}
.front .cta{left:0;width:387px;top:520px;text-align:center;color:#fff;font-size:9.5px;font-weight:700;letter-spacing:.3px}

/* inside left */
.problem-intro{background:linear-gradient(180deg,var(--navy) 0%,#1f4f8d 45%,var(--pale) 45%)}
.problem-intro .headline{left:34px;top:28px;color:#fff;font-weight:800;font-size:15px;line-height:1.15}
.problem-intro .body{left:34px;top:74px;width:320px;color:#e4ecf6;font-size:9.5px;line-height:1.4}
.problem-intro .body p+p{margin-top:10px}
.checklist{left:28px;top:198px;width:334px;height:240px;background:#eef3f9;border-radius:8px;padding:8px 12px}
.checklist .bar{background:var(--green-light);color:#fff;font-weight:700;font-size:11px;padding:5px 8px;border-radius:3px}
.checklist .ask{color:var(--blue);font-weight:800;font-size:10.5px;margin:9px 0 6px 4px}
.boxes{list-style:none;margin-left:4px}
.boxes li{display:flex;gap:9px;align-items:flex-start;font-size:9.5px;color:var(--ink);margin-bottom:8px;line-height:1.35}
.boxes li::before{content:"";width:12px;height:12px;border:1.3px solid #2d4f80;border-radius:2px;flex:none;background:#fff}
.checklist .verdict{font-size:9.5px;font-weight:700;color:var(--ink);line-height:1.4;margin:10px 0 0 4px}
.problem-intro .brand{left:66px;top:464px;color:var(--blue);font-size:24px}

/* inside right */
.compare{background:linear-gradient(180deg,#1b4c8c 0%,var(--navy) 100%)}
.compare .headline{left:20px;top:28px;color:#fff;font-weight:800;font-size:15px}
.compare .sub{left:20px;top:48px;color:#fff;font-size:10px;font-weight:600}
.compare .body{left:20px;top:66px;width:340px;color:#e4ecf6;font-size:9.5px;line-height:1.4}
.col{position:absolute;top:108px;width:164px;height:194px;border-radius:8px;padding:10px 10px;color:#fff}
.col.home{left:14px;background:var(--blue-box)}
.col.lab{left:200px;background:var(--green)}
.col h3{font-size:11px;font-weight:700;padding-bottom:6px;margin-bottom:8px;border-bottom:1.5px solid rgba(255,255,255,.8);display:inline-block}
.col ul{list-style:none}
.col li{margin-bottom:7px}
.col .pt{display:flex;align-items:center;gap:5px;font-size:10px;font-weight:700}
.col .pt .tick{background:#fff}
.col .pt .tick::after{border-color:var(--ink)}
.col.lab .pt .tick::after{border-color:var(--green)}
.col .note{font-size:7.5px;line-height:1.3;padding-left:15px;opacity:.92}
.vs{position:absolute;left:180px;top:178px;width:26px;height:26px;border-radius:50%;background:var(--navy);border:2px solid #fff;color:#fff;font-weight:800;font-size:10px;display:flex;align-items:center;justify-content:center}
</style>
</head>
<body>

<!-- OUTSIDE SPREAD -->
<section class="spread outside">
  <div class="panel left back">
    <svg class="abs" width="387" height="548" viewBox="0 0 387 548">
      <path d="M150 0 H387 V250 Q270 170 150 0 Z" fill="var(--photo-warm)" role="img" aria-label="Photo of a woman stretching after restful sleep in bed"/>
      <path d="M150 0 Q270 170 387 250" fill="none" stroke="var(--green)" stroke-width="5"/>
      <path d="M138 0 Q262 182 387 264" fill="none" stroke="var(--blue)" stroke-width="6"/>
      <path d="M0 548 L387 548 L387 470 Q340 500 300 548 Z" fill="var(--navy-deep)" opacity=".5"/>
    </svg>
    <div class="brand">Harborline CPAP<small>and Sleep Technology</small></div>
    <div class="photo-frame" style="left:38px;top:108px;width:136px;height:96px;background:var(--photo-cool)" role="img" aria-label="Photo of a man sleeping with sleep study sensors attached"></div>
    <div class="photo-frame" style="left:182px;top:108px;width:136px;height:96px;background:#b9c4d0" role="img" aria-label="Photo of a man sleeping wearing a CPAP mask"></div>
    <div class="abs headline">SLEEP APNEA TEST RESULTS IN LESS THAN 72 HOURS</div>
    <div class="abs lede">Skip the labs, skip the stress, just a simple test at home. $189 with results from board certified sleep physicians</div>
    <div class="abs rule"></div>
    <div class="contact phone">
      <svg width="16" height="16" viewBox="0 0 24 24"><path d="M6.6 10.8a15 15 0 0 0 6.6 6.6l2.2-2.2a1 1 0 0 1 1-.25 11.4 11.4 0 0 0 3.6.57 1 1 0 0 1 1 1V20a1 1 0 0 1-1 1A17 17 0 0 1 3 4a1 1 0 0 1 1-1h3.5a1 1 0 0 1 1 1c0 1.25.2 2.45.57 3.6a1 1 0 0 1-.25 1z" fill="var(--green)"/></svg>
      123-456-7890
    </div>
    <div class="contact web">
      <svg width="12" height="12" viewBox="0 0 12 12"><circle cx="6" cy="6" r="6" fill="var(--green)"/><circle cx="6" cy="6" r="3.2" fill="none" stroke="#fff" stroke-width="1"/><path d="M2.8 6h6.4" stroke="#fff" stroke-width="1"/></svg>
      www.harborlinecpap.com
    </div>
    <div class="contact mail">
      <svg width="12" height="12" viewBox="0 0 12 12"><circle cx="6" cy="6" r="6" fill="var(--green)"/><rect x="3" y="4" width="6" height="4.2" fill="none" stroke="#fff" stroke-width="1"/><path d="M3 4l3 2.4L9 4" fill="none" stroke="#fff" stroke-width="1"/></svg>
      info@harborlinecpap.com
    </div>
    <div class="contact addr">
      <svg width="12" height="14" viewBox="0 0 12 14"><path d="M6 0a5 5 0 0 1 5 5c0 3.5-5 9-5 9S1 8.5 1 5a5 5 0 0 1 5-5z" fill="var(--green)"/><circle cx="6" cy="5" r="1.8" fill="#fff"/></svg>
      <span>48 Linden Row, Suite 210, Fairview,<br>NY 10010</span>
    </div>
  </div>

  <div class="panel right front">
    <svg class="abs" width="387" height="548" viewBox="0 0 387 548">
      <path d="M0 0 H387 V205 Q230 250 0 165 Z" fill="#f1ece8" role="img" aria-label="Photo of a smiling woman waking up refreshed in white bedding"/>
      <path d="M0 172 Q230 258 387 212" fill="none" stroke="var(--navy)" stroke-width="6"/>
      <path d="M0 184 Q230 270 387 222" fill="none" stroke="var(--green)" stroke-width="6"/>
      <path d="M0 548 V512 Q200 470 387 478 V548 Z" fill="var(--navy)"/>
      <path d="M0 508 Q200 466 387 474" fill="none" stroke="var(--green)" stroke-width="4"/>
    </svg>
    <div class="brand">Harborline CPAP<small>and Sleep Technology</small></div>
    <div class="abs title"><span class="l1">BETTER SLEEP</span><span class="l2">STARTS AT HOME</span></div>
    <div class="abs tagline">Simple. Comfortable. Accurate Home Sleep Study.</div>
    <div class="abs facts">
      <ul class="tick-list">
        <li><span class="tick"></span>FDA CLEARED DEVICE, DOT APPROVED.</li>
        <li><span class="tick"></span>RESULTS IN LESS THAN 72 HOURS</li>
        <li><span class="tick"></span>98 PERCENT LAB ACCURACY</li>
      </ul>
    </div>
    <div class="abs cta">ORDER YOUR HOME SLEEP STUDY TODAY</div>
  </div>
</section>

<!-- INSIDE SPREAD -->
<section class="spread inside">
  <div class="panel left problem-intro">
    <div class="abs headline">80% OF SLEEP APNEACASES<br>GO UNDIAGNOSED.</div>
    <div class="abs body">
      <p>You wake up exhausted. You fall asleep at your desk. Your partner says you stop breathing at night. You know something's wrong.</p>
      <p>Most people wait years before getting tested because sleep labs are expensive, inconvenient, and scheduled months out. Meanwhile you're crashing your car, destroying your health, and feeling like garbage every single day.</p>
    </div>
    <div class="abs checklist">
      <div class="bar">SELF ASSESSMENT CHECKLIST</div>
      <div class="ask">DO YOU</div>
      <ul class="boxes">
        <li>Snore loudly?</li>
        <li>Wake up gasping or choking?</li>
        <li>Fall asleep during the day even when you<br>slept 8 hours?</li>
        <li>Wake up with headaches?</li>
        <li>Feel tired no matter how much you sleep?</li>
      </ul>
      <div class="verdict">If you checked 2 boxes, you probably have sleep<br>apnea. Stop guessing. Get tested.</div>
    </div>
    <div class="brand">Harborline CPAP<small>and Sleep Technology</small></div>
  </div>

  <div class="panel right compare">
    <svg class="abs" width="387" height="548" viewBox="0 0 387 548">
      <path d="M0 330 Q200 270 387 290 V548 H0 Z" fill="#eef2f6"/>
      <path d="M150 548 Q150 360 387 318 V548 Z" fill="#d9d6d3" role="img" aria-label="Photo of a hand resting on a bed with a pulse oximeter sensor"/>
      <path d="M0 322 Q200 262 387 282" fill="none" stroke="var(--green)" stroke-width="5"/>
      <path d="M140 548 Q140 352 387 308" fill="none" stroke="var(--navy)" stroke-width="5"/>
      <path d="M128 548 Q130 342 387 298" fill="none" stroke="var(--green)" stroke-width="3"/>
    </svg>
    <div class="abs headline">THE PROBLEM</div>
    <div class="abs sub">Sleep care wasn't built with people in mind.</div>
    <div class="abs body">Most people wait months, spend a fortune and end up feeling more like a chart than a human. It doesn't have to be this way.</div>
    <div class="col home">
      <h3>HOME SLEEP STUDY</h3>
      <ul>
        <li><div class="pt"><span class="tick"></span>Comfortable</div><div class="note">A minimal device with 2 wires and 3 sensors</div></li>
        <li><div class="pt"><span class="tick"></span>Convenient</div><div class="note">Delivered to your door - sleep in your own bed at home</div></li>
        <li><div class="pt"><span class="tick"></span>Accessible</div><div class="note">Scheduling and device delivery in 2 - 4 business days</div></li>
        <li><div class="pt"><span class="tick"></span>Affordable</div><div class="note">Pay a one-time flat fee of $189</div></li>
      </ul>
    </div>
    <div class="col lab">
      <h3>IN-LAB TESTING</h3>
      <ul>
        <li><div class="pt"><span class="tick"></span>Invasive</div><div class="note">20-30 wires attached all over your body</div></li>
        <li><div class="pt"><span class="tick"></span>Disruptive</div><div class="note">Must sleep in a lab overnight and requires travel</div></li>
        <li><div class="pt"><span class="tick"></span>Hard to schedule</div><div class="note">Scheduling can take anywhere from 3 weeks to 6 months</div></li>
        <li><div class="pt"><span class="tick"></span>Expensive</div><div class="note">Fees can range from $500 - $10,000</div></li>
      </ul>
    </div>
    <div class="vs">VS</div>
  </div>
</section>

</body>
</html>
```